Product Infographic 15-IN-1 Functional Coffee

prepare a infographic based upon the attached rough concept. please see the deck and packaging for branding

```html
<!DOCTYPE html>
<html lang="en">
<head>
<meta charset="utf-8">
<title>15-in-1 Functional Coffee</title>
<link rel="stylesheet" href="https://fonts.googleapis.com/css2?family=Bebas+Neue&family=Rubik:wght@400&display=swap">
<style>
  :root {
    --bg-deep: #0c2529;
    --bg-top: #17454b;
    --teal-panel: #339c9b;
    --mint: #6cc595;
    --mint-title: #5fbf8a;
    --ink-dark: #1a3a3c;
    --white: #ffffff;
    --icon-fill: #112d33;
    --coffee-dark: #7a4a28;
    --coffee-light: #e3c2a0;
    --pack-teal: #2f8f8c;
    --pack-red: #c8262c;
  }
  * { margin: 0; padding: 0; box-sizing: border-box; }
  html, body { width: 1200px; height: 849px; overflow: hidden; background: var(--bg-deep); }
  .canvas {
    position: relative; width: 1200px; height: 849px; overflow: hidden;
    background: linear-gradient(180deg, var(--bg-top) 0%, var(--bg-deep) 30%, var(--bg-deep) 100%);
    font-family: "Rubik", sans-serif;
  }
  .headline {
    position: absolute; top: 28px; left: 0; width: 1215px; text-align: center;
    font-family: "Bebas Neue", sans-serif; font-size: 74px; line-height: 1; color: var(--white);
    letter-spacing: 0.5px;
  }
  .subhead {
    position: absolute; top: 116px; left: 0; width: 1200px; text-align: center;
    font-family: "Bebas Neue", sans-serif; font-size: 48px; line-height: 1; color: var(--mint-title);
  }
  .foliage-band {
    position: absolute; left: 0; bottom: 0; width: 1200px; height: 170px;
    background: linear-gradient(180deg, rgba(40,120,120,0) 0%, rgba(40,130,125,0.45) 55%, rgba(60,150,140,0.6) 100%);
  }
  .connectors { position: absolute; inset: 0; }
  .glass {
    position: absolute; left: 506px; top: 181px; width: 186px; height: 571px;
    border-radius: 6px 6px 14px 14px;
    background: linear-gradient(100deg, var(--coffee-light) 0%, var(--coffee-dark) 35%, var(--coffee-light) 55%, #a36a3e 80%, var(--coffee-light) 100%);
    opacity: 0.95;
  }
  .benefits { position: absolute; left: 41px; top: 296px; width: 340px; }
  .benefit {
    height: 55px; margin-bottom: 12px; border-radius: 9px; background: var(--mint);
    padding: 9px 0 0 11px;
  }
  .benefit-title {
    font-family: "Bebas Neue", sans-serif; font-size: 22px; line-height: 1; color: var(--ink-dark);
  }
  .benefit-detail { font-size: 14px; line-height: 1.2; color: var(--white); margin-top: 1px; }
  .ingredient-panel {
    position: absolute; left: 901px; top: 135px; width: 281px; height: 505px;
    border-radius: 10px; background: var(--teal-panel);
  }
  .panel-brand {
    position: absolute; top: 28px; left: 0; width: 100%; padding-left: 30px; text-align: center;
    font-family: "Bebas Neue", sans-serif; font-size: 26px; color: var(--white);
  }
  .ingredient-list {
    position: absolute; left: 73px; top: 84px; list-style: none;
    font-family: "Bebas Neue", sans-serif; font-size: 20.5px; line-height: 27.7px; color: var(--white);
  }
  .pack {
    position: absolute; left: 430px; top: 544px; width: 199px; height: 236px; border-radius: 10px 10px 4px 4px;
    background: linear-gradient(180deg, var(--pack-teal) 0%, var(--pack-teal) 38%, var(--pack-red) 52%, var(--pack-red) 100%);
  }
  .brand-lockup {
    position: absolute; left: 31px; top: 745px; display: flex; align-items: center; gap: 10px;
  }
  .brand-dot { width: 66px; height: 66px; border-radius: 50%; border: 2px solid var(--white); }
  .brand-name {
    font-family: "Bebas Neue", sans-serif; font-size: 36px; line-height: 0.95; color: var(--white); width: 120px;
  }
</style>
</head>
<body>
<main class="canvas">
  <h1 class="headline">Your 15-in-1 Life Partner</h1>
  <h2 class="subhead">Functional Coffee</h2>

  <div class="foliage-band" role="img" aria-label="Band of coffee plant leaves along the bottom edge"></div>

  <div class="glass" role="img" aria-label="Tall glass of iced coffee swirled with cream"></div>

  <svg class="connectors" width="1200" height="849" viewBox="0 0 1200 849">
    <g stroke="#6cc595" stroke-width="3" fill="none">
      <line x1="381" y1="324" x2="544" y2="261"/>
      <line x1="381" y1="389" x2="564" y2="364"/>
      <line x1="381" y1="456" x2="555" y2="454"/>
      <line x1="381" y1="524" x2="564" y2="524"/>
      <line x1="380" y1="612" x2="506" y2="742"/>
    </g>
    <g fill="#6cc595">
      <circle cx="544" cy="261" r="8"/>
      <circle cx="564" cy="364" r="8"/>
      <circle cx="555" cy="454" r="8"/>
      <circle cx="564" cy="524" r="8"/>
    </g>
    <g stroke="#5fb5b0" stroke-width="1">
      <line x1="875" y1="236" x2="667" y2="280"/>
      <line x1="875" y1="300" x2="672" y2="337"/>
      <line x1="875" y1="365" x2="676" y2="382"/>
      <line x1="875" y1="428" x2="656" y2="428"/>
      <line x1="875" y1="492" x2="686" y2="469"/>
      <line x1="875" y1="557" x2="670" y2="516"/>
      <line x1="875" y1="620" x2="664" y2="555"/>
    </g>
  </svg>

  <section class="benefits">
    <div class="benefit"><div class="benefit-title">Elevated Mood - Sense of Wellbeing</div><div class="benefit-detail">Nootropics + Adaptogens</div></div>
    <div class="benefit" style="padding-left:23px"><div class="benefit-title">Focus &amp; Cognitive Performance</div><div class="benefit-detail">Nootropics</div></div>
    <div class="benefit" style="padding-left:19px"><div class="benefit-title">Decreased Stress &amp; Anxiety</div><div class="benefit-detail">Hemp Extracts + Adaptogens</div></div>
    <div class="benefit" style="padding-left:24px"><div class="benefit-title">Increased &amp; Sustained Energy</div><div class="benefit-detail">Energy Boosters</div></div>
    <div class="benefit" style="padding-left:24px"><div class="benefit-title">Nutrition</div><div class="benefit-detail">Protein, Healthy Fats, Vitamins</div></div>
  </section>

  <section class="ingredient-panel">
    <div class="panel-brand">Stoke &amp; Summit</div>
    <ul class="ingredient-list">
      <li>Organic Instant Coffee</li>
      <li>Hemp Derived THC</li>
      <li>Hemp Derived CBD</li>
      <li>Grass Fed Collagen Protein</li>
      <li>C8-C10 MCT Oil</li>
      <li>Organic Coffeeberry Extract</li>
      <li>L-Theanine</li>
      <li>Ashwagandha</li>
      <li>Bacopa Monnier</li>
      <li>Rhodiola</li>
      <li>Natural Caffein</li>
      <li>Organic ATP Booster</li>
      <li>Electrolytes</li>
      <li>Vitamin B6</li>
      <li>Vitamin B12</li>
    </ul>
  </section>

  <svg class="connectors" width="1200" height="849" viewBox="0 0 1200 849">
    <g fill="#112d33" stroke="#ffffff" stroke-width="1.5">
      <circle cx="901" cy="235" r="26"/>
      <circle cx="901" cy="299" r="26"/>
      <circle cx="901" cy="364" r="26"/>
      <circle cx="901" cy="428" r="26"/>
      <circle cx="901" cy="492" r="26"/>
      <circle cx="901" cy="557" r="26"/>
      <circle cx="901" cy="621" r="26"/>
    </g>
    <g fill="none" stroke="#ffffff" stroke-width="1.6" stroke-linecap="round">
      <path d="M890 234 h20 v6 a10 8 0 0 1 -20 0 z M910 236 h4 a3 3 0 0 1 0 6 h-4"/>
      <path d="M900 308 c-12 -4 -14 -14 -12 -20 c8 2 12 8 12 20 c0 -12 4 -18 12 -20 c2 6 0 16 -12 20z"/>
      <circle cx="901" cy="364" r="5"/><path d="M890 374 h22"/>
      <path d="M889 428 h24 a12 10 0 0 1 -24 0z"/>
      <path d="M901 504 v-22 M901 490 l-7 -6 M901 494 l7 -6"/>
      <path d="M901 569 c-10 -6 -10 -18 0 -24 c10 6 10 18 0 24z"/>
      <circle cx="901" cy="621" r="10"/>
    </g>
  </svg>

  <div class="pack" role="img" aria-label="Pouch of instant functional coffee blend"></div>

  <div class="brand-lockup">
    <div class="brand-dot"></div>
    <div class="brand-name">Stoke &amp; Summit</div>
  </div>
</main>
</body>
</html>
```